Gourmet butcher shop needs a business card design

We need a business card design for an upmarket butcher shop in Brisbane, Queensland Australia. We would prefer the card to be printed on a brown craft paper business card and would consider the use of raised print on the card. The card needs to make space for the usual information: ABN, address, telephone, facebook page. I stress it is a gourmet shop in a wealthy suburb. Thanks

Industry/Entity Type

Business

Contact Information for Business Card

Address Shop 5, Marrowbank Arcade, 417 Hollister Road, Wrenhurst
Telephone 07 3581 4927
A.B.N. 53 874 910 326
Facebook www.facebook.com/quillbyprimecuts

Requirements
Should not have
• No need for a person's name or title

```html
<!DOCTYPE html>
<html lang="en">
<head>
<meta charset="utf-8">
<title>Quillby Prime Cuts – Business Card</title>
<link rel="stylesheet" href="https://fonts.googleapis.com/css2?family=Open+Sans:wght@400;600;800&display=swap">
<style>
  :root {
    --backdrop: #6a4a36;
    --card: #1c1c1d;
    --card-edge: #141415;
    --emboss: #2c2c2e;
    --ink-light: #f2f2f2;
    --accent: #c8202f;
  }
  html, body {
    margin: 0;
    padding: 0;
    width: 1200px;
    height: 1000px;
    overflow: hidden;
    background: var(--backdrop);
    font-family: "Open Sans", Arial, sans-serif;
  }
  .canvas {
    position: relative;
    width: 1200px;
    height: 1000px;
  }
  .card {
    position: absolute;
    left: 265px;
    width: 666px;
    height: 397px;
    background: var(--card);
    border: 1px solid var(--card-edge);
    box-sizing: border-box;
  }
  .card--front { top: 73px; }
  .card--back { top: 532px; }

  .front-name {
    position: absolute;
    left: 0;
    right: 0;
    top: 130px;
    margin: 0;
    text-align: center;
    color: var(--emboss);
    font-weight: 800;
    text-transform: uppercase;
    line-height: 1;
    white-space: nowrap;
  }
  .front-name__line {
    display: block;
    font-size: 40px;
    letter-spacing: 3px;
  }
  .front-name__line--large {
    font-size: 62px;
    letter-spacing: 3px;
    margin-top: 12px;
  }

  .back-name {
    position: absolute;
    left: 52px;
    top: 150px;
    width: 268px;
    margin: 0;
    text-align: center;
    color: var(--ink-light);
    font-weight: 800;
    text-transform: uppercase;
    line-height: 1;
    white-space: nowrap;
  }
  .back-name__line {
    display: block;
    font-size: 21px;
    letter-spacing: 1px;
  }
  .back-name__line--large {
    font-size: 38px;
    letter-spacing: 1px;
    margin-top: 10px;
  }

  .contact {
    position: absolute;
    left: 378px;
    top: 136px;
    color: var(--ink-light);
    font-size: 15px;
    line-height: 22px;
    white-space: nowrap;
  }
  .contact__row {
    display: flex;
    align-items: center;
    gap: 8px;
  }
  .contact__row--spaced { margin-top: 7px; }
  .contact__icon {
    width: 16px;
    height: 14px;
    flex: none;
  }
  .contact__label { font-weight: 600; margin-right: 6px; }
  .contact__address { margin-top: 12px; }
</style>
</head>
<body>
<main class="canvas">
  <section class="card card--front" aria-label="Card front">
    <h1 class="front-name">
      <span class="front-name__line">Quillby</span>
      <span class="front-name__line front-name__line--large">Prime Cuts</span>
    </h1>
  </section>

  <section class="card card--back" aria-label="Card back">
    <h2 class="back-name">
      <span class="back-name__line">Quillby</span>
      <span class="back-name__line back-name__line--large">Prime Cuts</span>
    </h2>

    <div class="contact">
      <div class="contact__row">
        <svg class="contact__icon" viewBox="0 0 16 14" aria-hidden="true">
          <path fill="var(--accent)" d="M1 4c0-2 3-3 7-3s7 1 7 3v1h-3V3.6C11 3.2 9.5 3 8 3s-3 .2-4 .6V5H1z"/>
          <path fill="var(--accent)" d="M4 6h8l2 3v4H2V9z"/>
          <circle cx="8" cy="9.5" r="1.6" fill="var(--card)"/>
        </svg>
        <span>07 3581 4927</span>
      </div>
      <div class="contact__row">
        <svg class="contact__icon" viewBox="0 0 16 14" aria-hidden="true">
          <rect x="1" y="2" width="14" height="10" fill="var(--accent)"/>
          <path d="M1 2l7 6 7-6" fill="none" stroke="var(--card)" stroke-width="1.4"/>
        </svg>
        <span>quillbyprimecuts</span>
      </div>
      <div class="contact__row contact__row--spaced">
        <span><span class="contact__label">ABN</span> 53 874 910 326</span>
      </div>
      <div class="contact__address">
        Shop 5, Marrowbank Arcade, 417<br>
        Hollister Road, Wrenhurst
      </div>
    </div>
  </section>
</main>
</body>
</html>
```